Redesign of business card for Birchline Mechanical

We are looking for a new design for our business cards for Birchline Mechanical. We are a plumbing & HVAC construction company, operating on the West Coast of Canada and USA. Logo attached.
Industry/Entity Type
Construction - Plumbing & HVAC
Contact Information for Business Card
Name, address, phone numbers, email, website address
Look and feel
Each slider illustrates characteristics of the customer's brand and the style your logo design should communicate.

```html
<!DOCTYPE html>
<html lang="en">
<head>
<meta charset="utf-8">
<title>Birchline Mechanical – Business Card</title>
<link rel="stylesheet" href="https://fonts.googleapis.com/css2?family=Oswald:wght@500;700&family=Roboto:wght@300;400&display=swap">
<style>
  :root {
    --backdrop: #2a2a2c;
    --card: #1b1c1e;
    --card-edge: #111214;
    --ink: #ffffff;
    --rule: #6b6c70;
    --pattern-light: #26272a;
    --pattern-dark: #131416;
  }
  * { margin: 0; padding: 0; box-sizing: border-box; }
  html, body { width: 1200px; height: 1108px; overflow: hidden; }
  body {
    background: var(--backdrop);
    position: relative;
    font-family: "Roboto", sans-serif;
    color: var(--ink);
  }
  .card {
    position: absolute;
    top: 214px;
    width: 460px;
    height: 680px;
    background: var(--card);
    border-radius: 26px;
    box-shadow: 0 18px 40px rgba(0,0,0,.45);
  }
  .card--front { left: 90px; }
  .card--back { left: 650px; overflow: hidden; }

  .brand {
    position: absolute;
    top: 110px;
    left: 0; right: 0;
    display: flex;
    align-items: center;
    justify-content: center;
    gap: 14px;
  }
  .brand__mark {
    width: 22px; height: 22px;
    background: var(--ink);
  }
  .brand__name {
    font-family: "Oswald", sans-serif;
    font-weight: 500;
    font-size: 30px;
    letter-spacing: 2px;
    text-transform: uppercase;
  }

  .person {
    position: absolute;
    top: 290px;
    left: 0; right: 0;
    text-align: center;
  }
  .person__name {
    font-family: "Oswald", sans-serif;
    font-weight: 700;
    font-size: 40px;
    letter-spacing: .5px;
    text-transform: uppercase;
    line-height: 1.05;
  }
  .person__title {
    font-weight: 300;
    font-size: 21px;
    letter-spacing: 1px;
    text-transform: uppercase;
  }

  .rule {
    position: absolute;
    left: 100px; right: 100px;
    height: 1px;
    background: var(--rule);
  }
  .rule--top { top: 392px; }
  .rule--bottom { top: 590px; }

  .icons {
    position: absolute;
    top: 408px;
    left: 0; right: 0;
    display: flex;
    justify-content: center;
    gap: 8px;
  }
  .icon {
    width: 30px; height: 30px;
    background: var(--ink);
    border-radius: 5px;
    display: flex; align-items: center; justify-content: center;
  }

  .contact {
    position: absolute;
    top: 450px;
    left: 0; right: 0;
    text-align: center;
    font-size: 22px;
    line-height: 1.5;
    font-weight: 400;
  }
  .address {
    position: absolute;
    top: 605px;
    left: 0; right: 0;
    text-align: center;
    font-size: 21px;
    line-height: 1.4;
  }

  .pattern {
    position: absolute;
    inset: 0;
    background: linear-gradient(160deg, var(--pattern-light) 0%, var(--pattern-dark) 70%);
  }
  .back-brand {
    position: absolute;
    top: 470px;
    left: 0; right: 0;
    text-align: center;
    font-family: "Oswald", sans-serif;
    font-weight: 500;
    font-size: 18px;
    letter-spacing: 2px;
    text-transform: uppercase;
  }
</style>
</head>
<body>
  <section class="card card--front">
    <div class="brand">
      <span class="brand__mark"></span>
      <span class="brand__name">Birchline Mechanical</span>
    </div>

    <div class="person">
      <h1 class="person__name">Marcus Delaney</h1>
      <p class="person__title">Managing Director</p>
    </div>

    <div class="rule rule--top"></div>

    <div class="icons">
      <span class="icon" aria-label="Phone">
        <svg width="18" height="18" viewBox="0 0 24 24"><path fill="#1b1c1e" d="M6.6 10.8a15 15 0 0 0 6.6 6.6l2.2-2.2c.3-.3.7-.4 1-.2 1.1.4 2.3.6 3.6.6.6 0 1 .4 1 1V20c0 .6-.4 1-1 1A17 17 0 0 1 3 4c0-.6.4-1 1-1h3.5c.6 0 1 .4 1 1 0 1.3.2 2.5.6 3.6.1.3 0 .7-.2 1z"/></svg>
      </span>
      <span class="icon" aria-label="Email">
        <svg width="18" height="18" viewBox="0 0 24 24"><rect x="3" y="6" width="18" height="12" fill="none" stroke="#1b1c1e" stroke-width="2"/><path d="M3 6l9 7 9-7" fill="none" stroke="#1b1c1e" stroke-width="2"/></svg>
      </span>
      <span class="icon" aria-label="Website">
        <svg width="18" height="18" viewBox="0 0 24 24"><circle cx="12" cy="12" r="9" fill="none" stroke="#1b1c1e" stroke-width="2"/><path d="M3 12h18M12 3c3 3 3 15 0 18M12 3c-3 3-3 15 0 18" fill="none" stroke="#1b1c1e" stroke-width="1.6"/></svg>
      </span>
    </div>

    <div class="contact">
      <p>044-987 650 312</p>
      <p>info@birchlinemech.com</p>
      <p>www.birchlinemech.com</p>
    </div>

    <div class="rule rule--bottom"></div>

    <div class="address">
      <p>218, Cedar Harbour Road</p>
      <p>V6B 2K4, Canada</p>
    </div>
  </section>

  <section class="card card--back">
    <div class="pattern" role="img" aria-label="Tone-on-tone repeating brand pattern across the card back"></div>
    <p class="back-brand">Birchline</p>
  </section>
</body>
</html>
```